Business Card Design Project for Architecture and Interior Design company

We need a business card design and logo for an architecture and design firm located in Santiago de Chile. It´s a small company, and the name is "Ostrevo" ("Ostr" from my surname Ostrini, and "arq" for arquitectura or architecture. But it would also be nice that the logo comunicates de Word game "Bella" as beautiful in italian, and "arq" as architecture".
The idea is to give a delicate, elegant and sofisticated, yet fresh image. Would prefer grey black and white colors, but wouldn´t mind to use another additional color.
I allready have a web page www.ostrevo-studio.example, but would like to improve the logo design.
Please contact if any further information is requiered.
Reason: Need a more arquitectural and desing spirit in the cards. Few of them give that idea.

```html
<!DOCTYPE html>
<html lang="en">
<head>
<meta charset="utf-8">
<title>Ostrevo business card</title>
<link rel="stylesheet" href="https://fonts.googleapis.com/css2?family=Questrial&display=swap">
<style>
  :root {
    --backdrop: #707073;
    --paper: #f1f1f0;
    --paper-edge: #e7e7e6;
    --ink: #2a2a2c;
    --ink-soft: #3b3b3e;
  }
  * { margin: 0; padding: 0; box-sizing: border-box; }
  html, body {
    width: 1200px;
    height: 901px;
    overflow: hidden;
    background: var(--backdrop);
    font-family: "Questrial", "Helvetica Neue", Arial, sans-serif;
    color: var(--ink);
  }
  .card {
    position: absolute;
    left: 328px;
    width: 536px;
    height: 306px;
    background: radial-gradient(circle at 40% 40%, var(--paper) 0%, var(--paper-edge) 100%);
    overflow: hidden;
  }
  .card--front { top: 54px; }
  .card--back { top: 470px; }

  .brand-name {
    position: absolute;
    letter-spacing: 0.22em;
    text-transform: uppercase;
    color: var(--ink);
    white-space: nowrap;
    line-height: 1;
  }
  .card--front .brand-name {
    left: 0; right: 0;
    top: 165px;
    text-align: center;
    font-size: 42px;
    padding-left: 0.22em;
  }
  .website {
    position: absolute;
    left: 0; right: 0;
    top: 273px;
    text-align: center;
    font-size: 15px;
    line-height: 1;
    letter-spacing: 0.08em;
    color: var(--ink-soft);
  }
  .card--back .brand-name {
    right: 24px;
    top: 48px;
    font-size: 19px;
  }
  .person {
    position: absolute;
    left: 10px;
    top: 204px;
    width: 130px;
    text-align: right;
  }
  .person__name {
    font-size: 30px;
    line-height: 1;
    letter-spacing: 0.2em;
    color: var(--ink-soft);
    margin-right: -0.2em;
  }
  .person__role {
    font-size: 14px;
    line-height: 1;
    letter-spacing: 0.15em;
    color: var(--ink-soft);
    margin-top: 6px;
    margin-right: -0.15em;
  }
  .divider {
    position: absolute;
    left: 145px;
    top: 179px;
    width: 1px;
    height: 101px;
    background: var(--ink-soft);
  }
  .contact {
    position: absolute;
    left: 155px;
    top: 196px;
    list-style: none;
    font-size: 16px;
    line-height: 21px;
    letter-spacing: 0.05em;
    color: var(--ink-soft);
    white-space: nowrap;
  }
</style>
</head>
<body>
  <section class="card card--front">
    <div class="brand-name">Ostrevo</div>
    <p class="website">ostrevo-studio.example</p>
  </section>

  <section class="card card--back">
    <div class="brand-name">Ostrevo</div>
    <div class="person">
      <p class="person__name">NAME</p>
      <p class="person__role">CEO</p>
    </div>
    <div class="divider"></div>
    <ul class="contact">
      <li>address: 218 Calle Norte, Santiago</li>
      <li>phone: 600-12-48</li>
      <li>email: hello@ostrevo-studio.example</li>
    </ul>
  </section>
</body>
</html>
```